Powerpoint master slide deck for power point presentation by members of my company

To design a master slide deck for powerpoint presentation for a Orthopaedic Clinic Based in Singapore

```html
<!DOCTYPE html>
<html lang="en">
<head>
<meta charset="utf-8">
<title>Jointwell Orthopaedics – Slide Master</title>
<link href="https://fonts.googleapis.com/css2?family=Roboto:wght@400;500&family=Roboto+Slab:wght@600;700&display=swap" rel="stylesheet">
<style>
  :root{
    --stage:#2a2a2a;
    --slide:#e8f5f5;
    --blob:#c4e3dc;
    --blob-light:#f5fbfb;
    --navy:#1b3a5c;
    --pill:#8fcbb5;
    --badge:#8fcbb5;
    --coral:#ef6868;
    --mint:#8cc7b3;
    --logo-text:#5b6c79;
    --logo-mark:#5fb3ac;
  }
  *{box-sizing:border-box;margin:0;padding:0}
  html,body{width:1200px;height:1200px;overflow:hidden}
  body{background:var(--stage);position:relative;font-family:'Roboto',sans-serif}
  .slide{position:absolute;width:544px;height:306px;background:var(--slide);overflow:hidden;box-shadow:0 6px 18px rgba(0,0,0,.45)}
  .slide--title{left:43px;top:267px}
  .slide--intro{left:612px;top:267px}
  .slide--section{left:43px;top:627px}
  .slide--contents{left:612px;top:627px}
  .blob{position:absolute;border-radius:50%}
  .blob--teal{background:var(--blob)}
  .blob--light{background:var(--blob-light)}
  .brand{position:absolute;display:flex;align-items:center;gap:6px;color:var(--logo-text);font-family:'Roboto',sans-serif;font-weight:400;white-space:nowrap}
  .brand__mark{background:var(--logo-mark);flex:none}
  .brand--large{left:44px;top:34px;font-size:20px;gap:10px}
  .brand--large .brand__mark{width:36px;height:36px}
  .brand--small{font-size:10.5px;top:11px}
  .brand--small .brand__mark{width:18px;height:18px}
  .brand--right{right:17px}
  .brand--left{left:16px}
  .art{position:absolute;border-radius:14px}
  .heading{font-family:'Roboto Slab',serif;font-weight:700;color:var(--navy);position:absolute}
  .pill{position:absolute;background:var(--pill);color:var(--navy);border-radius:14px;font-size:12.5px;display:flex;align-items:center;justify-content:center;letter-spacing:.1px;white-space:nowrap}
  .plus{position:absolute;width:10px;height:10px}
  .plus::before,.plus::after{content:"";position:absolute;background:currentColor;border-radius:1px}
  .plus::before{left:35%;top:0;width:30%;height:100%}
  .plus::after{top:35%;left:0;height:30%;width:100%}
  .plus--coral{color:var(--coral)}
  .plus--mint{color:var(--mint)}
  .plus--white{color:#fff}
  .plus--sm{width:7px;height:7px}
  .plus--lg{width:13px;height:13px}

  .title-main{right:52px;top:74px;text-align:right;font-size:30px;line-height:33px}
  .intro-heading{left:0;width:384px;top:91px;text-align:center;font-size:27px}
  .intro-text{position:absolute;left:72px;width:240px;top:139px;text-align:center;font-size:11.2px;line-height:14.6px;color:var(--navy)}
  .section-badge{position:absolute;left:144px;top:80px;width:58px;height:58px;border-radius:50%;background:var(--badge);display:flex;align-items:center;justify-content:center;font-family:'Roboto Slab',serif;font-weight:700;font-size:27px;color:var(--navy)}
  .section-heading{left:0;width:346px;top:145px;text-align:center;font-size:37px}
  .contents-heading{left:47px;top:38px;font-size:24px;font-weight:600}
  .toc-item{position:absolute;display:flex;gap:11px;width:190px}
  .toc-item__num{flex:none;width:46px;height:46px;border-radius:50%;background:var(--badge);display:flex;align-items:center;justify-content:center;font-family:'Roboto Slab',serif;font-weight:700;font-size:20px;color:var(--navy);margin-top:5px}
  .toc-item__title{font-family:'Roboto Slab',serif;font-weight:600;font-size:15px;color:var(--navy);line-height:18px;white-space:nowrap}
  .toc-item__text{font-size:10.4px;line-height:13px;color:var(--navy);margin-top:4px;width:105px}
</style>
</head>
<body>

<section class="slide slide--title">
  <div class="blob blob--light" style="left:165px;top:-60px;width:170px;height:95px"></div>
  <div class="blob blob--teal" style="left:-50px;top:160px;width:240px;height:200px"></div>
  <div class="blob blob--light" style="left:410px;top:255px;width:180px;height:110px"></div>
  <div class="brand brand--large"><span class="brand__mark"></span>Jointwell Orthopaedics</div>
  <span class="plus plus--mint" style="left:495px;top:23px"></span>
  <span class="plus plus--coral plus--lg" style="left:503px;top:46px"></span>
  <span class="plus plus--white plus--sm" style="left:478px;top:45px"></span>
  <span class="plus plus--coral" style="left:108px;top:103px"></span>
  <span class="plus plus--mint plus--sm" style="left:31px;top:115px"></span>
  <div class="art" role="img" aria-label="Illustration of a physiotherapist helping a patient stretch a knee on an exercise mat" style="left:16px;top:152px;width:248px;height:124px;background:linear-gradient(160deg,#e8a64a 0%,#f2a23a 55%,#6d9fc2 100%)"></div>
  <h1 class="heading title-main">Hospital<br>Resident Practice<br>Medical Center</h1>
  <div class="pill" style="left:272px;top:215px;width:230px;height:24px">Here is where your presentation begins</div>
</section>

<section class="slide slide--intro">
  <div class="blob blob--teal" style="left:-90px;top:-60px;width:135px;height:170px"></div>
  <div class="blob blob--light" style="left:-30px;top:245px;width:80px;height:90px"></div>
  <div class="blob blob--teal" style="left:360px;top:160px;width:230px;height:220px"></div>
  <div class="brand brand--small brand--right"><span class="brand__mark"></span>Jointwell Orthopaedics</div>
  <span class="plus plus--coral plus--sm" style="left:470px;top:54px"></span>
  <span class="plus plus--mint plus--sm" style="left:395px;top:67px"></span>
  <span class="plus plus--coral" style="left:65px;top:234px"></span>
  <span class="plus plus--mint plus--sm" style="left:111px;top:259px"></span>
  <h2 class="heading intro-heading">Introduction</h2>
  <p class="intro-text">You can give a brief description of the topic you want to talk about here. For example, if you want to talk about Mercury, you can say that it’s the smallest planet in the entire Solar System</p>
  <div class="art" role="img" aria-label="Illustration of a therapist adjusting the posture of a patient seated on an exercise ball" style="left:332px;top:84px;width:177px;height:161px;background:linear-gradient(150deg,#f2b13a 0%,#d44848 50%,#6f9fc8 100%)"></div>
</section>

<section class="slide slide--section">
  <div class="blob blob--light" style="left:10px;top:-70px;width:170px;height:125px"></div>
  <div class="blob blob--teal" style="left:357px;top:235px;width:200px;height:130px"></div>
  <div class="blob blob--teal" style="left:470px;top:160px;width:150px;height:170px"></div>
  <div class="brand brand--small brand--left"><span class="brand__mark"></span>Jointwell Orthopaedics</div>
  <div class="section-badge">01</div>
  <h2 class="heading section-heading">Our center</h2>
  <div class="pill" style="left:42px;top:202px;width:261px;height:24px;font-size:12px">You can enter a subtitle here if you need it</div>
  <span class="plus plus--white plus--lg" style="left:336px;top:77px"></span>
  <span class="plus plus--mint plus--sm" style="left:379px;top:89px"></span>
  <span class="plus plus--coral" style="left:326px;top:122px"></span>
  <span class="plus plus--coral" style="left:30px;top:273px"></span>
  <div class="art" role="img" aria-label="Isometric illustration of a doctor examining a patient's leg on a treatment table beside cabinets" style="left:326px;top:65px;width:199px;height:221px;background:linear-gradient(155deg,#f4f6f7 0%,#ee7a6e 45%,#8cc9b2 75%,#9a9fa6 100%)"></div>
</section>

<section class="slide slide--contents">
  <div class="blob blob--light" style="left:383px;top:-70px;width:180px;height:140px"></div>
  <div class="blob blob--teal" style="left:-40px;top:250px;width:190px;height:110px"></div>
  <div class="brand brand--small brand--right"><span class="brand__mark"></span>Jointwell Orthopaedics</div>
  <h2 class="heading contents-heading">Table of contents</h2>
  <span class="plus plus--coral" style="left:503px;top:53px"></span>
  <span class="plus plus--white plus--lg" style="left:52px;top:81px"></span>
  <span class="plus plus--coral" style="left:20px;top:132px"></span>
  <span class="plus plus--mint plus--sm" style="left:94px;top:124px"></span>
  <div class="art" role="img" aria-label="Illustration of a doctor in a white coat holding a clipboard" style="left:34px;top:118px;width:65px;height:168px;background:linear-gradient(180deg,#ffffff 0%,#f2f4f5 55%,#1f3c63 100%)"></div>
  <div class="toc-item" style="left:131px;top:113px">
    <div class="toc-item__num">01</div>
    <div><div class="toc-item__title">Our center</div><p class="toc-item__text">You can describe the topic of the section here</p></div>
  </div>
  <div class="toc-item" style="left:326px;top:113px">
    <div class="toc-item__num">02</div>
    <div><div class="toc-item__title">Key numbers</div><p class="toc-item__text">You can describe the topic of the section here</p></div>
  </div>
  <div class="toc-item" style="left:131px;top:198px">
    <div class="toc-item__num">03</div>
    <div><div class="toc-item__title">Patient care</div><p class="toc-item__text">You can describe the topic of the section here</p></div>
  </div>
  <div class="toc-item" style="left:326px;top:198px">
    <div class="toc-item__num">04</div>
    <div><div class="toc-item__title">Our success</div><p class="toc-item__text">You can describe the topic of the section here</p></div>
  </div>
</section>

</body>
</html>
```